Corvana Wound Care Business card design

We need a business card designed around our logo which was provided. The logo of preference is the colored. Also the colors and fonts were provided.

Target Market(s)

Our Referral partners are home health agencies.

Industry/Entity Type

Healthcare

Contact Information for Business Card

Name , Phone #, Email , Title

Requirements
Nice to have
• Creativity
Should not have
• basic

```html
<!DOCTYPE html>
<html lang="en">
<head>
<meta charset="UTF-8">
<title>Corvana Wound Care – Business Card</title>
<link href="https://fonts.googleapis.com/css2?family=Montserrat:wght@400;500&family=Tinos:wght@400;700&display=swap" rel="stylesheet">
<style>
  :root {
    --stage: #232323;
    --card: #181818;
    --card-back: #141414;
    --blue-deep: #2b3f9e;
    --blue-mid: #1565c0;
    --blue-bright: #0aa6ec;
    --ink-light: #f2f2f2;
    --rule: #e6e6e6;
  }
  * { box-sizing: border-box; margin: 0; padding: 0; }
  html, body {
    width: 1200px; height: 800px; overflow: hidden;
    background: var(--stage);
  }
  .stage {
    position: relative; width: 1200px; height: 800px;
    display: flex; align-items: center; justify-content: center; gap: 40px;
  }
  .card {
    position: relative; width: 540px; height: 310px;
    border-radius: 26px; overflow: hidden;
    box-shadow: 0 18px 40px rgba(0,0,0,.55);
  }

  /* Back side */
  .card--back { background: var(--card-back); }
  .back-pattern {
    position: absolute; inset: 0;
    background: linear-gradient(200deg, #6f6f6f 0%, #3b3b3b 30%, #151515 60%, #050505 100%);
  }
  .back-brand {
    position: absolute; left: 250px; top: 150px;
    font-family: "Tinos", serif; font-weight: 700; font-size: 30px;
    color: var(--blue-mid); display: flex; align-items: center; gap: 10px;
  }
  .brand-mark {
    width: 20px; height: 20px; border-radius: 4px; background: var(--blue-mid);
  }

  /* Front side */
  .card--front { background: var(--card); }
  .front-brand {
    position: absolute; left: 34px; top: 40px;
    font-family: "Tinos", serif; font-weight: 700; font-size: 32px;
    color: var(--blue-mid); display: flex; align-items: center; gap: 12px;
  }
  .front-brand .brand-mark { width: 24px; height: 24px; }
  .person {
    position: absolute; right: 40px; top: 92px; text-align: right;
  }
  .person__name {
    font-family: "Tinos", serif; font-weight: 400; font-size: 25px;
    letter-spacing: .5px; text-transform: uppercase;
    background: linear-gradient(90deg, var(--blue-deep), var(--blue-bright));
    -webkit-background-clip: text; background-clip: text; color: transparent;
  }
  .person__title {
    font-family: "Montserrat", sans-serif; font-size: 15px;
    color: var(--ink-light); margin-top: 2px;
  }
  .accent-tab {
    position: absolute; right: 0; top: 88px; width: 12px; height: 42px;
    background: linear-gradient(180deg, var(--blue-bright), var(--blue-mid));
  }
  .divider {
    position: absolute; left: 34px; right: 34px; top: 160px;
    height: 1px; background: var(--rule);
  }
  .contacts {
    position: absolute; left: 34px; top: 176px; list-style: none;
    font-family: "Tinos", serif; font-size: 16px; color: var(--ink-light);
  }
  .contacts li { display: flex; align-items: center; gap: 12px; height: 26px; }
  .contacts svg { width: 17px; height: 17px; fill: var(--blue-bright); }
  .address {
    position: absolute; right: 40px; top: 182px; text-align: right;
    font-family: "Tinos", serif; font-size: 16px; line-height: 1.45;
    color: var(--ink-light);
  }
  .bottom-band {
    position: absolute; left: 0; right: 0; bottom: 0; height: 16px;
  }
</style>
</head>
<body>
<main class="stage">

  <section class="card card--back" aria-label="Card back">
    <div class="back-pattern" role="img" aria-label="Decorative pattern of glossy cross shapes fading from grey to black"></div>
    <div class="back-brand"><span class="brand-mark"></span>Corvana Wound Care</div>
  </section>

  <section class="card card--front" aria-label="Card front">
    <div class="front-brand"><span class="brand-mark"></span>Corvana Wound Care</div>

    <div class="accent-tab"></div>
    <div class="person">
      <p class="person__name">Marcus Ellery</p>
      <p class="person__title">Owner</p>
    </div>

    <div class="divider"></div>

    <ul class="contacts">
      <li>
        <svg viewBox="0 0 24 24" aria-hidden="true"><path d="M6.6 10.8a15.1 15.1 0 0 0 6.6 6.6l2.2-2.2a1 1 0 0 1 1-.25 11.4 11.4 0 0 0 3.6.57 1 1 0 0 1 1 1V20a1 1 0 0 1-1 1A17 17 0 0 1 3 4a1 1 0 0 1 1-1h3.5a1 1 0 0 1 1 1c0 1.25.2 2.45.57 3.57a1 1 0 0 1-.25 1z"/></svg>
        0415 738 260
      </li>
      <li>
        <svg viewBox="0 0 24 24" aria-hidden="true"><path d="M2 5h20v14H2z M2 5l10 8 10-8" /></svg>
        hello@corvanacare.com
      </li>
      <li>
        <svg viewBox="0 0 24 24" aria-hidden="true"><path d="M12 2a10 10 0 1 0 0 20 10 10 0 0 0 0-20zm6.9 6h-3a15.7 15.7 0 0 0-1.3-3.9A8 8 0 0 1 18.9 8zM12 4c.8 1.2 1.5 2.5 1.9 4h-3.8c.4-1.5 1.1-2.8 1.9-4zM4.3 14a8 8 0 0 1 0-4h3.4a16 16 0 0 0 0 4zm.8 2h3a15.7 15.7 0 0 0 1.3 3.9A8 8 0 0 1 5.1 16zm3-8h-3a8 8 0 0 1 4.3-3.9A15.7 15.7 0 0 0 8.1 8zM12 20c-.8-1.2-1.5-2.5-1.9-4h3.8c-.4 1.5-1.1 2.8-1.9 4zm2.3-6H9.7a14.6 14.6 0 0 1 0-4h4.6a14.6 14.6 0 0 1 0 4zm.3 5.9a15.7 15.7 0 0 0 1.3-3.9h3a8 8 0 0 1-4.3 3.9zM16.3 14a16 16 0 0 0 0-4h3.4a8 8 0 0 1 0 4z"/></svg>
        www.corvanacare.com
      </li>
    </ul>

    <p class="address">88, Harbor Lane Suite 4<br>20731, Northfield</p>

    <svg class="bottom-band" viewBox="0 0 540 16" preserveAspectRatio="none" aria-hidden="true">
      <defs>
        <linearGradient id="band-fill" x1="0" x2="1">
          <stop offset="0" stop-color="#2b3f9e"/>
          <stop offset=".5" stop-color="#0aa6ec"/>
          <stop offset="1" stop-color="#2b3f9e"/>
        </linearGradient>
      </defs>
      <polygon points="0,8 238,8 246,0 540,0 540,16 0,16" fill="url(#band-fill)"/>
      <polygon points="246,0 262,0 254,8 238,8" fill="#18a0e6"/>
    </svg>
  </section>

</main>
</body>
</html>
```